Broschüren-Design für Organisation gesucht
Zielgruppe
Infos zu unserer Organisation finden Sie unter: http://www.velquor.net
Aufgabenstellung
Unsere NGO veröffentlicht ein survey report. Auf diesem Wege suchen wir designer, die das Report professionel gestalten. Das Report ist angehängt.

```html
<!DOCTYPE html>
<html lang="en">
<head>
<meta charset="utf-8">
<title>Opinion Polling Report – Cover and Spread</title>
<link rel="stylesheet" href="https://fonts.googleapis.com/css2?family=Source+Sans+3:wght@400;600;700&family=Source+Serif+4:wght@400&display=swap">
<style>
  :root {
    --bg: #1f55a0;
    --paper: #ffffff;
    --brand-blue: #2150a2;
    --soft-blue: #6f8fc6;
    --label-blue: #8fa6d4;
    --track: #e1e1e1;
    --map-tint: #f3f3f3;
    --green: #2eab6a;
    --ink: #222222;
    --row: #ececec;
  }
  * { margin: 0; padding: 0; box-sizing: border-box; }
  html, body { width: 848px; height: 1200px; overflow: hidden; }
  body { background: var(--bg); font-family: "Source Sans 3", sans-serif; color: var(--ink); position: relative; }

  .cover { position: absolute; left: 259px; top: 74px; width: 335px; height: 474px; background: var(--paper); overflow: hidden; }
  .cover-map { position: absolute; left: 4px; top: 48px; width: 328px; height: 300px; background: var(--map-tint); border-radius: 40px 90px 60px 120px; }
  .brand { position: absolute; left: 107px; top: 38px; display: flex; align-items: center; gap: 4px; }
  .brand-mark { width: 16px; height: 16px; border: 1.5px solid var(--brand-blue); }
  .brand-name { font-size: 6.5px; font-weight: 400; color: var(--brand-blue); line-height: 1.15; text-transform: uppercase; width: 100px; }
  .charts { position: absolute; left: 0; top: 0; }
  .pct { font-family: "Source Sans 3", sans-serif; font-weight: 700; font-size: 15px; }
  .cover-title { position: absolute; left: 63px; top: 328px; font-size: 12.5px; font-weight: 700; color: var(--brand-blue); line-height: 1.35; letter-spacing: 0.3px; text-transform: uppercase; }
  .cover-date { position: absolute; left: 63px; top: 367px; font-size: 6px; line-height: 1.4; }
  .cover-contact { position: absolute; left: 63px; top: 431px; font-family: "Source Serif 4", serif; font-size: 5px; line-height: 1.4; }

  .spread { position: absolute; left: 161px; top: 726px; width: 526px; height: 384px; display: flex; }
  .page { position: relative; width: 263px; height: 384px; background: var(--paper); overflow: hidden; }
  .page-left { background: linear-gradient(to right, #ffffff 88%, #ececec); }
  .page-right { background: linear-gradient(to left, #ffffff 88%, #ececec); }
  .deco { position: absolute; top: 8px; width: 68px; height: 70px; border-radius: 8px; }
  .deco-green { left: 14px; background: linear-gradient(135deg, #34b574, var(--green)); }
  .deco-blue { left: 181px; background: linear-gradient(135deg, #2a5cb0, var(--brand-blue)); }
  .section-title { position: absolute; font-size: 12px; font-weight: 600; line-height: 1.35; text-transform: uppercase; letter-spacing: 0.2px; }
  .who-title { left: 45px; top: 98px; }
  .exec-title { left: 49px; top: 32px; }
  .columns { position: absolute; display: flex; gap: 9px; font-size: 3.9px; line-height: 1.4; }
  .columns p + p { margin-top: 4px; }
  .columns .col { width: 80px; text-align: justify; }
  .who-cols { left: 45px; top: 140px; }
  .exec-cols { left: 49px; top: 84px; }
  .page-num { position: absolute; top: 348px; font-size: 10px; font-weight: 600; }
  .num-left { left: 33px; }
  .num-right { left: 220px; }

  .results { position: absolute; left: 49px; top: 200px; width: 169px; border-collapse: collapse; font-size: 4.6px; }
  .results th { background: var(--brand-blue); color: #fff; font-weight: 600; height: 12px; }
  .results td { height: 12px; }
  .results tr:nth-child(even) td { background: var(--row); }
  .results .idx { color: var(--brand-blue); width: 12px; text-align: center; font-weight: 700; }
  .results .val { text-align: center; }
  .footnote { position: absolute; left: 49px; top: 324px; width: 170px; font-family: "Source Serif 4", serif; font-size: 3.2px; line-height: 1.4; text-align: justify; }
</style>
</head>
<body>

<section class="cover">
  <div class="cover-map" role="img" aria-label="Faint map of Afghanistan in the background"></div>
  <div class="brand">
    <span class="brand-mark"></span>
    <span class="brand-name">Velquor Social Research Organization</span>
  </div>
  <svg class="charts" width="335" height="474" viewBox="0 0 335 474">
    <g transform="rotate(-90 248 138)">
      <circle cx="248" cy="138" r="34" fill="none" stroke="var(--track)" stroke-width="24"/>
      <circle cx="248" cy="138" r="34" fill="none" stroke="var(--soft-blue)" stroke-width="24" stroke-dasharray="192.3 213.6"/>
    </g>
    <g transform="rotate(-90 64 212)">
      <circle cx="64" cy="212" r="31" fill="none" stroke="var(--track)" stroke-width="22"/>
      <circle cx="64" cy="212" r="31" fill="none" stroke="var(--brand-blue)" stroke-width="22" stroke-dasharray="116.9 194.8"/>
    </g>
    <g transform="rotate(-90 236 256)">
      <circle cx="236" cy="256" r="32.5" fill="none" stroke="var(--track)" stroke-width="23"/>
      <circle cx="236" cy="256" r="32.5" fill="none" stroke="var(--brand-blue)" stroke-width="23" stroke-dasharray="153.2 204.2"/>
    </g>
    <text class="pct" x="239" y="84" fill="var(--label-blue)" text-anchor="middle" dominant-baseline="central">90%</text>
    <text class="pct" x="43" y="208" fill="var(--soft-blue)" text-anchor="middle" dominant-baseline="central">60%</text>
    <text class="pct" x="213" y="236" fill="var(--soft-blue)" text-anchor="middle" dominant-baseline="central">75%</text>
  </svg>
  <h1 class="cover-title">Opinion Polling for the<br>Afghan Presidential&nbsp; Election 2019</h1>
  <p class="cover-date">July 11, 2019<br>Kabul, Afghanistan</p>
  <p class="cover-contact">Velquor Social Research Organization&nbsp; Sector 7,<br>Kabul, Afghanistan<br>E-mail: info@velquor.af</p>
</section>

<section class="spread">
  <article class="page page-left">
    <div class="deco deco-green" role="img" aria-label="Green abstract decorative shape"></div>
    <h2 class="section-title who-title">Who we are</h2>
    <div class="columns who-cols">
      <div class="col">
        <p>The Velquor Social Research Organization (VELQUOR) is a nonpartisan and independent non-governmental organization based in Kabul. At VELQUOR, we conduct public opinion polls, demographic research, content analysis and a variety of data-driven research.</p>
        <p>Our mission is to facilitate fact based transparency to support sustainable development, good governance and to promote democracy by producing high-quality evidence-based social science research. We study Afghan public attitude, demographic trends, policy impact, communication and public relations with the help of the latest</p>
      </div>
      <div class="col">
        <p>technology as well as standardized and customized methodology to enable intelligent decision-making processes. In order to convey the right message from complex and large data, we focus on presenting the general public and our clients with easy to read and comprehensible virtualization and visualization tools.</p>
        <p>VELQUOR relies on its pool of national and international experts to carry out the following activities: conducting independent, high-quality research and analysis; advising governments, international organisations and the NGO sector; and informing and encouraging public debate.</p>
      </div>
    </div>
    <span class="page-num num-left">01</span>
  </article>

  <article class="page page-right">
    <div class="deco deco-blue" role="img" aria-label="Blue abstract decorative shape"></div>
    <h2 class="section-title exec-title">Executive<br>Summary</h2>
    <div class="columns exec-cols">
      <div class="col">
        <p>In order to investigate the public attitude and preference towards the upcoming Afghan presidential election and the presidential candidates, VELQUOR conducted a survey between 30 March 2019 - 25 May 2019 that was representative of the Afghan population.</p>
        <p>The poll adopted the probability-based sampling approach, a standard technique applied by almost all public pollsters which is the cornerstone of modern survey research. An intelligent algorithm generated random valid phone numbers and a team of professional interviewers conducted phone interviews to capture the views of the sample population. The survey process was supported by a specifically designed</p>
      </div>
      <div class="col">
        <p>survey management system. The representative sample size of 2405 is calculated based on a margin of +/-2 percentage point sampling error and a confidence level of 95 percent. The sample was collected from 31 of the 34 provinces in Afghanistan and was reasonably balanced with regard to geographical location and ethnic composition. However the sample shows a gender imbalance since more men than women were sampled1.</p>
        <p>The participation rate is 81.1% which demonstrates people's willingness to take part in the survey and express their attitudes and preferences towards the upcoming presidential election. The final result of the survey is as below:</p>
      </div>
    </div>
    <table class="results">
      <thead>
        <tr><th colspan="2">Candidate</th><th>Percentage of Respondents' Votes</th></tr>
      </thead>
      <tbody>
        <tr><td class="idx">1</td><td>Farid Nasery</td><td class="val">35.1</td></tr>
        <tr><td class="idx">2</td><td>Karim Wahedi</td><td class="val">5.8</td></tr>
        <tr><td class="idx">3</td><td>Jawid Sarwari</td><td class="val">3.3</td></tr>
        <tr><td class="idx">4</td><td>Nasir Habibzai</td><td class="val">2.5</td></tr>
        <tr><td class="idx">5</td><td>Omid Rahyab</td><td class="val">1.2</td></tr>
        <tr><td class="idx">6</td><td>Others</td><td class="val">3.0</td></tr>
        <tr><td class="idx">7</td><td>Not specified</td><td class="val">5.9</td></tr>
        <tr><td class="idx">8</td><td>Not yet decided</td><td class="val">43.3</td></tr>
      </tbody>
    </table>
    <p class="footnote">1 The reason for this skewness may be twofold: firstly, if a household can afford only one mobile phone, it is more likely that the male head of the household will have primary access to that mobile phone and therefore be more likely to be sampled. Secondly, women are less likely to answer the phone if the caller is unknown. Hence, they are less likely to be sampled.</p>
    <span class="page-num num-right">02</span>
  </article>
</section>

</body>
</html>
```